Templates for Construction Company

We are looking to have templates prepared for all aspects of our letter sending. Using our brand design. with similar layouts that look the same.

Letterheads design & Email signatures

We use letter heads for - quotes, contract correspondence, variations, formal letters, invitations

Target Market(s)

Clients documents sent in emails

Industry/Entity Type

Construction

Font styles to use
Serif
Sans Serif

Colors
0054AA
0677BA
7BADD7
CADEEF
E8F1F8

Requirements
Must have
• Easy to read, water marks on page
Nice to have
• Different options for different letters

```html
<!DOCTYPE html>
<html lang="en">
<head>
<meta charset="utf-8">
<title>Stonefield Builders – Letterhead &amp; Email Signature</title>
<link href="https://fonts.googleapis.com/css2?family=Arimo:wght@400;700&display=swap" rel="stylesheet">
<style>
  :root {
    --brand-blue: #5487c4;
    --ink-grey: #5e5e5e;
    --rule-grey: #6a6a6a;
    --paper: #fafafb;
    --backdrop: #c4c4c4;
    --watermark: #eef0f3;
  }
  * { margin: 0; padding: 0; box-sizing: border-box; }
  html, body {
    width: 1200px; height: 1164px; overflow: hidden;
    background: var(--backdrop);
    font-family: 'Arimo', Arial, sans-serif;
    color: var(--ink-grey);
  }
  .canvas { position: relative; width: 1200px; height: 1164px; }

  .sheet {
    position: absolute;
    background: var(--paper);
    border-bottom-style: solid;
    border-bottom-color: var(--brand-blue);
  }

  /* Letterhead */
  .letterhead { left: 329px; top: 44px; width: 541px; height: 765px; border-bottom-width: 9px; }
  .brand {
    position: absolute; left: 0; right: 0;
    display: flex; align-items: center; justify-content: center; gap: 8px;
    color: var(--brand-blue); font-weight: 700; letter-spacing: -0.5px;
  }
  .brand-square { background: var(--ink-grey); flex: none; }
  .letterhead .brand { top: 86px; font-size: 30px; }
  .letterhead .brand-square { width: 16px; height: 16px; }

  .watermark {
    position: absolute; left: 0; right: 0; top: 390px;
    text-align: center; font-weight: 700; font-size: 72px;
    color: var(--watermark); letter-spacing: -1px;
  }

  .footer { position: absolute; left: 0; right: 0; text-align: center; }
  .letterhead .footer { top: 716px; font-size: 10px; }
  .address { display: block; }
  .rule { height: 1px; background: var(--rule-grey); margin: 0 auto; }
  .letterhead .rule { width: 312px; margin-top: 4px; margin-bottom: 5px; }
  .contacts { display: flex; justify-content: center; align-items: center; gap: 6px; }
  .contact { display: inline-flex; align-items: center; gap: 5px; white-space: nowrap; }
  .icon { fill: var(--brand-blue); flex: none; }
  .letterhead .icon { width: 9px; height: 9px; }

  /* Email signature */
  .signature { left: 239px; top: 860px; width: 721px; height: 232px; border-bottom-width: 12px; }
  .signature .brand { top: 28px; font-size: 52px; gap: 12px; }
  .signature .brand-square { width: 26px; height: 26px; }
  .person { position: absolute; left: 0; right: 0; top: 129px; text-align: center; font-size: 20px; }
  .person-name { color: var(--brand-blue); font-weight: 700; }
  .person-role { color: var(--ink-grey); }
  .signature .footer { top: 164px; font-size: 17px; }
  .signature .rule { width: 500px; margin-top: 5px; margin-bottom: 4px; }
  .signature .contacts { gap: 9px; }
  .signature .contact { gap: 8px; }
  .signature .icon { width: 15px; height: 15px; }
</style>
</head>
<body>
<svg width="0" height="0" style="position:absolute" aria-hidden="true">
  <defs>
    <symbol id="icon-phone" viewBox="0 0 24 24"><path d="M6.6 10.8a15.1 15.1 0 0 0 6.6 6.6l2.2-2.2a1 1 0 0 1 1-.25 11.4 11.4 0 0 0 3.6.57 1 1 0 0 1 1 1V20a1 1 0 0 1-1 1A17 17 0 0 1 3 4a1 1 0 0 1 1-1h3.5a1 1 0 0 1 1 1c0 1.25.2 2.45.57 3.57a1 1 0 0 1-.25 1z"/></symbol>
    <symbol id="icon-mail" viewBox="0 0 24 24"><path d="M2 5h20v14H2z M3.5 6.5 12 13l8.5-6.5" fill="currentColor"/><path d="M3 6l9 7 9-7" stroke="#fafafb" stroke-width="1.6" fill="none"/></symbol>
    <symbol id="icon-globe" viewBox="0 0 24 24"><circle cx="12" cy="12" r="10"/><path d="M2 12h20M12 2c3 3 3 17 0 20M12 2c-3 3-3 17 0 20" stroke="#fafafb" stroke-width="1.5" fill="none"/></symbol>
  </defs>
</svg>

<main class="canvas">
  <section class="sheet letterhead" aria-label="Letterhead">
    <div class="brand"><span class="brand-square"></span>Stonefield Builders</div>
    <div class="watermark" aria-hidden="true">Stonefield</div>
    <footer class="footer">
      <span class="address">Your address, city, state, ZIP 0000</span>
      <div class="rule"></div>
      <div class="contacts">
        <span class="contact"><svg class="icon"><use href="#icon-phone"/></svg>123-456-2100</span>
        <span class="contact"><svg class="icon"><use href="#icon-mail"/></svg>youremail@example.com</span>
        <span class="contact"><svg class="icon"><use href="#icon-globe"/></svg>www.yourwebsite.com</span>
      </div>
    </footer>
  </section>

  <section class="sheet signature" aria-label="Email signature">
    <div class="brand"><span class="brand-square"></span>Stonefield Builders</div>
    <p class="person"><span class="person-name">Daniel Hart |</span> <span class="person-role">Manager</span></p>
    <footer class="footer">
      <span class="address">Your address, city, state, ZIP 0000</span>
      <div class="rule"></div>
      <div class="contacts">
        <span class="contact"><svg class="icon"><use href="#icon-phone"/></svg>123-456-2100</span>
        <span class="contact"><svg class="icon"><use href="#icon-mail"/></svg>youremail@example.com</span>
        <span class="contact"><svg class="icon"><use href="#icon-globe"/></svg>www.yourwebsite.com</span>
      </div>
    </footer>
  </section>
</main>
</body>
</html>
```